Harlow Ridge Growers and Nursery needs a business street sign.

I have three businesses located at the same address: The Harlow Ridge Growers & Nursery, The Bramble Nook, and The Quarry Commons. I am looking for a 4’ x 8’ street sign to represent all three businesses as one retail experience. It needs to be eye catching yet simple enough that people can fully read it while driving by. I have logos for the greenhouse and village however I do not have anything for The Bramble Nook. I’m looking for some type of font that’s similar or in between the two attached logos for The Bramble Nook.

• Horizontal Sign, Eye catching, yet simple design so people see it while driving by.
• Horizontal Sign
• I’m open to the design being both vertical and horizontal. Please provide both options

```html
<!DOCTYPE html>
<html lang="en">
<head>
<meta charset="utf-8">
<title>Harlow Ridge Growers &amp; Nursery – Street Sign</title>
<link rel="stylesheet" href="https://fonts.googleapis.com/css2?family=Lexend:wght@600&display=swap">
<style>
  :root {
    --sand: #f2d3a2;
    --sand-deep: #e8bf82;
    --divider-light: #fbe7c6;
    --divider-tan: #d3b172;
    --leaf-green: #1b8a24;
    --mint: #5fd8b0;
    --petal-cream: #fbe3c2;
    --brick: #8d1616;
  }
  * { margin: 0; padding: 0; box-sizing: border-box; }
  html, body { width: 1200px; height: 2400px; overflow: hidden; background: var(--sand); }
  .sign { position: relative; width: 1200px; height: 2400px; background: var(--sand); }

  .pattern-band {
    position: absolute; left: 170px; width: 860px; height: 170px;
    background: radial-gradient(ellipse at center, var(--sand-deep) 0%, rgba(232,191,130,0.35) 60%, transparent 75%);
  }
  .pattern-band.top { top: 0; }
  .pattern-band.bottom { bottom: 0; }

  .flower-row {
    position: absolute;
    background: linear-gradient(90deg, var(--mint) 0%, #3ed07a 20%, var(--petal-cream) 45%, #44cfa0 65%, var(--petal-cream) 85%, #3fd3c4 100%);
  }
  .flower-row.top { left: 220px; top: 100px; width: 815px; height: 145px; border-radius: 70px 70px 0 0; }
  .flower-row.bottom { left: 155px; top: 2105px; width: 900px; height: 165px; border-radius: 0 0 80px 80px; }

  .panel-edge {
    position: absolute; left: 0; width: 1200px; height: 4px;
    background: linear-gradient(90deg, transparent, rgba(60,200,90,0.55) 20%, rgba(60,200,90,0.55) 80%, transparent);
  }
  .panel-edge.top { top: 243px; }
  .panel-edge.bottom { top: 2103px; }

  .divider { position: absolute; left: 0; width: 1200px; height: 22px;
    background: linear-gradient(var(--divider-light) 0 9px, var(--divider-tan) 9px 100%); }
  .divider.first { top: 918px; }
  .divider.second { top: 1400px; }

  .section { position: absolute; left: 0; width: 1200px; display: flex; flex-direction: column; align-items: center; justify-content: center; text-align: center; }
  .section.greenhouse { top: 245px; height: 673px; }
  .section.commons { top: 940px; height: 460px; }
  .section.bramble { top: 1422px; height: 683px; }

  .name-mark { font-family: "Lexend", sans-serif; font-weight: 600; line-height: 1.05; }
  .greenhouse .name-mark { color: var(--leaf-green); font-size: 108px; }
  .greenhouse .name-mark .small { font-size: 76px; display: block; }
  .commons .name-mark { color: var(--brick); font-size: 150px; }
  .commons .name-mark .small { font-size: 120px; display: block; }
  .bramble .name-mark { color: var(--leaf-green); font-size: 104px; white-space: nowrap; }
</style>
</head>
<body>
<main class="sign">
  <div class="pattern-band top" role="img" aria-label="Faint chrysanthemum petal pattern"></div>
  <div class="flower-row top" role="img" aria-label="Row of paper-cut flowers in green, teal and cream"></div>
  <div class="panel-edge top"></div>

  <section class="section greenhouse">
    <h1 class="name-mark">The Harlow Ridge<span class="small">Growers &amp; Nursery</span></h1>
  </section>

  <div class="divider first"></div>

  <section class="section commons">
    <h2 class="name-mark">Quarry<span class="small">Commons</span></h2>
  </section>

  <div class="divider second"></div>

  <section class="section bramble">
    <h2 class="name-mark">The Bramble Nook</h2>
  </section>

  <div class="panel-edge bottom"></div>
  <div class="flower-row bottom" role="img" aria-label="Row of paper-cut flowers in cream, green and teal"></div>
  <div class="pattern-band bottom" role="img" aria-label="Faint chrysanthemum petal pattern"></div>
</main>
</body>
</html>
```